Street Sign Project - Attract Customers

We need a street sign designed to display out the front of the building. It design will need to be 1800mm wide x 900mm high. We need to show potential customers where we are inviting. Some of the attachments are for inspiration. The sign will be printed on a sheet of aluminum. if you have a good look at our web site which is www.pk-r.com.au you should get a good feeling about the company and what we do.

Target Market(s)

Construction companies, landscaping and civil earth moving companies who may drive past our business

Industry/Entity Type

Building

Font styles to use
Sans Serif

Colors
ffffff
3277b5
000000

Requirements
Must have
• Company logo must be the main focus point
• The number "54" on the sign to show street number (300mm high)
• phone number - (02) 9418 3065
• web address - www.pk-r.com.au
• I have loaded pictures i would like to see used in the sign
Nice to have
• Banner picture as attached
Should not have
• Bright colours. Please use our blue colour where possible

```html
<!DOCTYPE html>
<html lang="en">
<head>
<meta charset="utf-8">
<title>Parkline Kran &amp; Rigging – Street Sign</title>
<link rel="stylesheet" href="https://fonts.googleapis.com/css2?family=Exo+2:wght@700;800&display=swap">
<style>
  :root {
    --brand-blue: #3277b5;
    --web-blue: #1f86d8;
    --text-grey: #6b6b6b;
    --white: #ffffff;
    --card-tan: #c9a878;
    --card-tan-dark: #a9865a;
    --belt-light: #e6ddd0;
    --belt-dark: #b9ad9c;
    --belt-blue: #1f5fc8;
  }
  html, body {
    margin: 0;
    padding: 0;
    overflow: hidden;
    background: var(--white);
  }
  .sign {
    position: relative;
    width: 1200px;
    height: 606px;
    overflow: hidden;
    background: var(--white);
    font-family: "Exo 2", Arial, sans-serif;
  }
  .brand {
    position: absolute;
    left: 28px;
    top: 24px;
    display: flex;
    align-items: center;
    gap: 14px;
    z-index: 2;
  }
  .brand-mark {
    width: 50px;
    height: 50px;
    background: var(--brand-blue);
    flex: none;
  }
  .brand-name {
    margin: 0;
    font-weight: 800;
    font-size: 48px;
    line-height: 1;
    color: var(--brand-blue);
    text-transform: uppercase;
    letter-spacing: 0.3px;
    white-space: nowrap;
  }
  .street-number {
    position: absolute;
    left: 22px;
    top: 78px;
    margin: 0;
    font-weight: 800;
    font-size: 270px;
    line-height: 0.86;
    color: var(--brand-blue);
    letter-spacing: -4px;
  }
  .address {
    position: absolute;
    left: 372px;
    top: 98px;
    margin: 0;
    font-weight: 700;
    font-size: 27px;
    color: var(--text-grey);
  }
  .phone {
    position: absolute;
    left: 372px;
    top: 134px;
    margin: 0;
    color: var(--text-grey);
    font-weight: 700;
    display: flex;
    align-items: baseline;
    gap: 8px;
  }
  .phone-label { font-size: 16px; }
  .phone-number { font-size: 34px; letter-spacing: 1px; }
  .website {
    position: absolute;
    right: 24px;
    bottom: 30px;
    margin: 0;
    font-weight: 700;
    font-size: 23px;
    color: var(--web-blue);
  }
  .illustration {
    position: absolute;
  }
  .carton {
    left: 0;
    top: 392px;
    width: 232px;
    height: 214px;
    background: linear-gradient(135deg, var(--card-tan), var(--card-tan-dark));
  }
  .carton-corner {
    right: 0;
    top: 0;
    width: 32px;
    height: 150px;
    background: linear-gradient(180deg, var(--card-tan), var(--card-tan-dark));
  }
  .conveyor {
    left: 560px;
    top: 150px;
    width: 640px;
    height: 456px;
  }
  .photo {
    position: absolute;
    background: var(--white);
    padding: 5px;
    box-shadow: 0 4px 10px rgba(0,0,0,0.35);
  }
  .photo-fill { width: 100%; height: 100%; }
  .photo-hopper {
    left: 224px; top: 330px; width: 336px; height: 256px;
    transform: rotate(-1deg);
  }
  .photo-hopper .photo-fill { background: linear-gradient(160deg, #e4e6ea, #9aa5b5 70%, #2f4f8a); }
  .photo-rubble {
    left: 560px; top: 206px; width: 262px; height: 290px;
    transform: rotate(-2deg);
  }
  .photo-rubble .photo-fill { background: linear-gradient(170deg, #7a7366, #bdb6aa 50%, #8a8378); }
  .photo-hoist {
    left: 800px; top: 96px; width: 218px; height: 256px;
    transform: rotate(-2deg);
  }
  .photo-hoist .photo-fill { background: linear-gradient(160deg, #b8c2cc, #5d86c2 55%, #3b5c94); }
  .photo-ladder {
    left: 968px; top: 8px; width: 194px; height: 226px;
    transform: rotate(-2deg);
  }
  .photo-ladder .photo-fill { background: linear-gradient(180deg, #6d8fc4, #b85a4a 40%, #e8e8e4 62%, #5f9a3e 88%); }
</style>
</head>
<body>
<main class="sign">
  <div class="illustration carton" role="img" aria-label="Open cardboard box"></div>
  <div class="illustration carton-corner" role="img" aria-label="Edge of a cardboard box"></div>

  <svg class="illustration conveyor" viewBox="0 0 640 456" role="img" aria-label="Roller conveyor belt running diagonally">
    <defs>
      <linearGradient id="beltFill" x1="0" y1="1" x2="1" y2="0">
        <stop offset="0" stop-color="var(--belt-light)"/>
        <stop offset="1" stop-color="var(--belt-dark)"/>
      </linearGradient>
    </defs>
    <polygon points="0,456 640,10 640,120 200,456" fill="url(#beltFill)"/>
    <polygon points="200,456 640,120 640,250 380,456" fill="var(--belt-blue)"/>
  </svg>

  <div class="photo photo-hopper"><div class="photo-fill" role="img" aria-label="Worker on scaffold operating a hoist with a hopper bucket"></div></div>
  <div class="photo photo-rubble"><div class="photo-fill" role="img" aria-label="Worker loading rubble onto a site conveyor"></div></div>
  <div class="photo photo-hoist"><div class="photo-fill" role="img" aria-label="Blue goods hoist mounted on building scaffold"></div></div>
  <div class="photo photo-ladder"><div class="photo-fill" role="img" aria-label="Ladder hoist reaching a tiled roof with solar panels"></div></div>

  <div class="brand">
    <span class="brand-mark" aria-hidden="true"></span>
    <h1 class="brand-name">Parkline Kran &amp; Rigging</h1>
  </div>

  <p class="street-number">54</p>
  <p class="address">Bramwell Street</p>
  <p class="phone"><span class="phone-label">Call</span><span class="phone-number">(02) 9418 3065</span></p>
  <p class="website">www.pk-r.com.au</p>
</main>
</body>
</html>
```